Stationery Design needed for logo design project

This project is linked to Logo: brand identity for modern furniture design studio..

Our company needs a Stationery Design. Please refer to our original project in the link above.

```html
<!DOCTYPE html>
<html lang="en">
<head>
<meta charset="utf-8">
<title>lumbra — Stationery</title>
<link rel="stylesheet" href="https://fonts.googleapis.com/css2?family=Questrial&display=swap">
<style>
  :root {
    --backdrop: #d3d3d3;
    --paper: #ffffff;
    --wood-light: #f7f7f7;
    --wood-mid: #ececec;
    --ink: #1a1a1a;
    --ink-soft: #444444;
    --flap-edge: #d0d0d0;
  }
  * { margin: 0; padding: 0; box-sizing: border-box; }
  html, body { width: 1200px; height: 889px; overflow: hidden; }
  body {
    position: relative;
    background: var(--backdrop);
    font-family: "Questrial", "Helvetica Neue", Arial, sans-serif;
    color: var(--ink);
  }
  .sheet {
    position: absolute;
    background: var(--paper);
    overflow: hidden;
    box-shadow: 0 2px 6px rgba(0,0,0,0.18);
  }
  .wood {
    position: absolute;
    inset: 0;
    background: linear-gradient(90deg, var(--wood-light) 0%, var(--wood-mid) 22%, var(--wood-light) 45%, var(--wood-mid) 70%, var(--wood-light) 100%);
  }
  .wood--faint { opacity: 0.45; }
  .brand {
    position: absolute;
    font-family: "Questrial", "Helvetica Neue", Arial, sans-serif;
    font-weight: 400;
    color: var(--ink);
    line-height: 1;
    letter-spacing: 0.01em;
    white-space: nowrap;
  }
  .bar { position: absolute; background: var(--ink); }
  .contact {
    position: absolute;
    color: var(--ink-soft);
    line-height: 1.3;
  }
  .contact .gap { display: block; height: 0.7em; }
  .contact .web { color: var(--ink); font-weight: 700; }

  /* Letterhead */
  .letterhead { left: 193px; top: 65px; width: 364px; height: 516px; }
  .letterhead .bar--top { left: 29px; top: 0; width: 145px; height: 7px; }
  .letterhead .bar--bottom { left: 0; bottom: 0; width: 100%; height: 6px; }
  .letterhead .brand { left: 28px; top: 20px; font-size: 52px; }
  .letterhead .contact { left: 29px; top: 416px; font-size: 7.5px; }

  /* Folder cover */
  .folder { left: 620px; top: 65px; width: 365px; height: 515px; }
  .folder .brand { left: 108px; top: 228px; font-size: 50px; }

  /* Business cards */
  .card-front { left: 62px; top: 625px; width: 165px; height: 94px; }
  .card-front .bar--top { left: 0; top: 0; width: 100%; height: 4px; }
  .card-front .brand { left: 32px; top: 28px; font-size: 38px; }

  .card-back { left: 62px; top: 744px; width: 165px; height: 94px; }
  .card-back .bar--side { left: 0; top: 39px; width: 4px; height: 18px; }
  .card-back .brand { left: 17px; top: 34px; font-size: 23px; }
  .card-back .divider { position: absolute; left: 86px; top: 21px; width: 1px; height: 54px; background: #bbbbbb; }
  .card-back .person { position: absolute; left: 93px; top: 21px; font-size: 6.5px; font-weight: 700; color: var(--ink); }
  .card-back .contact { left: 93px; top: 31px; font-size: 4.6px; }

  /* DL envelope front */
  .envelope-front { left: 268px; top: 622px; width: 409px; height: 216px; }
  .envelope-front .brand { left: 22px; top: 22px; font-size: 52px; }
  .envelope-front .contact { left: 246px; top: -4px; padding-top: 0; font-size: 7.5px; top: -1px; }
  .envelope-front .window {
    position: absolute; left: 23px; top: 115px; width: 148px; height: 62px;
    background: var(--paper); border-radius: 10px; box-shadow: inset 0 0 3px rgba(0,0,0,0.15);
  }

  /* Envelope back */
  .envelope-back { left: 715px; top: 622px; width: 409px; height: 216px; }
  .envelope-back .flap {
    position: absolute; left: 0; top: 0; width: 100%; height: 63px;
    border-radius: 0 0 26px 26px; overflow: hidden;
    box-shadow: 0 2px 4px var(--flap-edge);
  }
  .envelope-back .brand { left: 171px; top: 21px; font-size: 24px; }
</style>
</head>
<body>

  <section class="sheet letterhead" aria-label="Letterhead">
    <div class="wood wood--faint" role="img" aria-label="Pale whitewashed wood grain texture"></div>
    <div class="bar bar--top"></div>
    <div class="brand">lumbra</div>
    <p class="contact">
      Studio 4B<br>2040 Oak Lane,<br>Bristol, England.
      <span class="gap"></span>
      +44 (0) 555 010 200<br>hello@lumbra.com<br><span class="web">www.lumbra.com</span>
    </p>
    <div class="bar bar--bottom"></div>
  </section>

  <section class="sheet folder" aria-label="Presentation folder cover">
    <div class="wood" role="img" aria-label="Whitewashed wood plank texture"></div>
    <div class="brand">lumbra</div>
  </section>

  <section class="sheet card-front" aria-label="Business card front">
    <div class="wood" role="img" aria-label="Whitewashed wood grain texture"></div>
    <div class="bar bar--top"></div>
    <div class="brand">lumbra</div>
  </section>

  <section class="sheet card-back" aria-label="Business card back">
    <div class="bar bar--side"></div>
    <div class="brand">lumbra</div>
    <div class="divider"></div>
    <p class="person">Anna Reed</p>
    <p class="contact">
      Studio 4B<br>2040 Oak Lane,<br>Bristol, England.
      <span class="gap"></span>
      +44 (0) 555 010 200<br>hello@lumbra.com<br><span class="web">www.lumbra.com</span>
    </p>
  </section>

  <section class="sheet envelope-front" aria-label="Window envelope front">
    <div class="wood wood--faint" role="img" aria-label="Pale whitewashed wood grain texture"></div>
    <div class="brand">lumbra</div>
    <p class="contact" style="top: 0;">
      Studio 4B<br>2040 Oak Lane, Bristol, England.
      <span class="gap"></span>
      +44 (0) 555 010 200<br>hello@lumbra.com<br><span class="web">www.lumbra.com</span>
    </p>
    <div class="window"></div>
  </section>

  <section class="sheet envelope-back" aria-label="Envelope back">
    <div class="flap">
      <div class="wood" role="img" aria-label="Whitewashed wood grain texture on envelope flap"></div>
      <div class="brand">lumbra</div>
    </div>
  </section>

</body>
</html>
```